Fennel Cellar Online organic artisan and gourmet supermarket

Brief:
Brand: Fennel Cellar (FC) is an online store selling artisan and organinc Italian products. Our look and feel we have gone with is rustic, premium and unfiltered (visit us @ www.fennelcellar.com.au)
Our slogan: "cook Italy, eat Italy, love Italy"
Goals: prior to our online store going live, we used to attend a food market once a week. Due to unfortunate circumstances, we stopped. Since then, our store has gone live and wanted to use the card as a reminder we are back at the markets.
I also have a restaurant, "fennel ristorante" so I wanted to hand them out to customers in the restaurant but also act as reminder of our pop up market stores and our website to buy from.
Personality: FC is more than just a store. Our goal is to be not only a store but an informationa hub of Italian food.
We offer assistance to people who need help in their kitchen as well as catering
Logo: I have a logo which I was not able to upload.

Target Market(s)

Food lovers
Italian food interest
Wealthy
Organic gourmet food enthusiest

Industry/Entity Type

Store

Contact Information for Business Card

Shop online or visit us @ Willow Bend organic market
Ciao@fennelcellar.com.au
Www.fennelcellar.com.au

Online store, Cooking advice, catering, ristorante and information hub

Requirements
Must have
• Logo
• Information
• May be larger than a business card to fit information but smaller than a post card
• Need to look interesting and different
• Not a simple card design
Nice to have
• Different fonts
• Rustic looking
• Qwerky

```html
<!DOCTYPE html>
<html lang="en">
<head>
<meta charset="utf-8">
<title>Fennel Cellar – Business Card</title>
<link rel="stylesheet" href="https://fonts.googleapis.com/css2?family=Comic+Neue:wght@400;700&family=Noto+Serif:wght@400&family=Montserrat:wght@500&display=swap">
<style>
  :root {
    --page-bg: #e6e6e6;
    --card-dark: #141414;
    --card-mid: #2a2a2a;
    --photo-light: #5a5a5a;
    --ink-white: #f2f2f2;
    --ink-soft: #d8d8d8;
    --italy-green: #2f9a4c;
    --italy-red: #c7343a;
  }
  * { box-sizing: border-box; margin: 0; padding: 0; }
  html, body { width: 1200px; height: 1200px; overflow: hidden; }
  body {
    background: var(--page-bg);
    display: flex;
    flex-direction: column;
    align-items: center;
    justify-content: center;
    gap: 40px;
  }
  .card {
    position: relative;
    width: 960px;
    height: 545px;
    border-radius: 44px;
    overflow: hidden;
  }
  /* Front */
  .card-front .food-photo {
    position: absolute; inset: 0;
    background:
      radial-gradient(ellipse at 20% 25%, var(--photo-light) 0%, transparent 45%),
      radial-gradient(ellipse at 80% 70%, #444 0%, transparent 50%),
      linear-gradient(135deg, #3a3a3a 0%, #222 55%, #111 100%);
  }
  .brand-seal {
    position: absolute;
    left: 50%; top: 50%;
    width: 440px; height: 440px;
    transform: translate(-48%, -50%);
    border: 4px solid var(--ink-white);
    border-radius: 50%;
    display: flex; align-items: center; justify-content: center;
  }
  .brand-name {
    font-family: "Montserrat", sans-serif;
    font-weight: 500;
    font-size: 44px;
    letter-spacing: 4px;
    color: var(--ink-white);
    text-transform: uppercase;
    text-align: center;
    line-height: 1.2;
  }
  /* Back */
  .card-back {
    background:
      radial-gradient(ellipse at 75% 60%, var(--card-mid) 0%, transparent 55%),
      radial-gradient(ellipse at 15% 75%, #1f1f1f 0%, transparent 50%),
      var(--card-dark);
  }
  .card-back .faint-photo {
    position: absolute; inset: 0;
    background: linear-gradient(160deg, rgba(255,255,255,0.03), rgba(255,255,255,0));
  }
  .slogan {
    position: absolute;
    top: 58px; left: 0; right: 0;
    text-align: center;
    font-family: "Comic Neue", cursive;
    font-weight: 700;
    font-size: 52px;
    color: var(--ink-white);
    letter-spacing: 1px;
  }
  .slogan .cook { color: var(--italy-green); }
  .slogan .love { color: var(--italy-red); }
  .contact-list {
    position: absolute;
    top: 180px; left: 237px;
    list-style: none;
    font-family: "Noto Serif", serif;
    font-size: 27px;
    color: var(--ink-soft);
  }
  .contact-list li {
    display: flex; align-items: center;
    gap: 22px;
    height: 55px;
  }
  .contact-list svg { width: 28px; height: 28px; flex: none; }
  .services {
    position: absolute;
    bottom: 42px; left: 122px; right: 110px;
    display: flex;
    list-style: none;
  }
  .service {
    display: flex; flex-direction: column; align-items: center;
    width: 168px;
    font-family: "Noto Serif", serif;
    font-size: 21px;
    color: var(--ink-white);
  }
  .service:last-child { margin-left: auto; width: 150px; }
  .service svg { width: 96px; height: 86px; margin-bottom: 4px; }
</style>
</head>
<body>

<section class="card card-front" aria-label="Card front">
  <div class="food-photo" role="img" aria-label="Black and white photograph of Italian deli food on a rustic wooden board"></div>
  <div class="brand-seal">
    <p class="brand-name">Fennel<br>Cellar</p>
  </div>
</section>

<section class="card card-back" aria-label="Card back">
  <div class="faint-photo" role="img" aria-label="Faint dark photograph of Italian food"></div>

  <p class="slogan">"<span class="cook">cook Italy,</span> eat Italy, <span class="love">love Italy</span>"</p>

  <ul class="contact-list">
    <li>
      <svg viewBox="0 0 24 24" fill="none" stroke="#d8d8d8" stroke-width="2"><path d="M12 22s-7-7-7-12a7 7 0 0 1 14 0c0 5-7 12-7 12z"/><circle cx="12" cy="10" r="2.5"/></svg>
      48 Larch Lane, Westmere, 2087
    </li>
    <li>
      <svg viewBox="0 0 24 24" fill="none" stroke="#d8d8d8" stroke-width="1.6"><rect x="2" y="5" width="20" height="14"/><path d="M2 5l10 8 10-8M2 19l7-7M22 19l-7-7"/></svg>
      ciao@fennelcellar.com.au
    </li>
    <li>
      <svg viewBox="0 0 24 24" fill="#d8d8d8"><path d="M6.6 3.5l2.6 3.4-1.6 2.2c.9 2.3 2.8 4.3 5.3 5.4l2.2-1.6 3.4 2.6-1.4 3c-7.4-.4-12.8-6-13.1-13.2z"/></svg>
      www.fennelcellar.com.au
    </li>
  </ul>

  <ul class="services">
    <li class="service">
      <svg viewBox="0 0 96 86" fill="none" stroke="#f2f2f2" stroke-width="3"><rect x="2" y="2" width="92" height="82" rx="8"/><path d="M18 22h10l8 32h34l6-24H30"/><path d="M40 34v16M50 34v16M60 34v16"/><circle cx="40" cy="64" r="4"/><circle cx="66" cy="64" r="4"/></svg>
      Online
    </li>
    <li class="service">
      <svg viewBox="0 0 96 86" fill="none" stroke="#f2f2f2" stroke-width="3"><rect x="2" y="2" width="92" height="82" rx="8"/><path d="M20 58a28 28 0 0 1 56 0z"/><path d="M14 62h68"/><circle cx="48" cy="26" r="3"/></svg>
      Caterine
    </li>
    <li class="service">
      <svg viewBox="0 0 96 86" fill="none" stroke="#f2f2f2" stroke-width="3"><rect x="2" y="2" width="92" height="82" rx="8"/><circle cx="50" cy="43" r="20"/><circle cx="50" cy="43" r="12"/><path d="M18 18v18M14 18v12a4 4 0 0 0 8 0V18M18 36v32"/><path d="M82 18c-5 4-5 14 0 20v30"/></svg>
      Ristorante
    </li>
    <li class="service">
      <svg viewBox="0 0 96 86" fill="none" stroke="#f2f2f2" stroke-width="3"><rect x="2" y="2" width="92" height="82" rx="8"/><path d="M34 16h28v16H34z"/><path d="M38 32v8h20v-8"/><path d="M30 70c0-14 8-20 18-20s18 6 18 20"/><path d="M56 62h18l-4 10H60z"/></svg>
      Cooking Advice
    </li>
  </ul>
</section>

</body>
</html>
```